Our Pantry Remedy

I am a pharmacist turn chef and my current website www.ourpantryremedy-demo.com is in desperate need of a make over. I want to be able to add how to videos, photographs and have tabs. The tabs needed will be Home, About, Recipes, Health & Wellness, Services, Confidentiality, Affordability, Blog, Articles and Friday Cocktails. Eventually I will want a news letter, but do not want that now, only the ability to add it later. I will also want to add a market place tab later to sell merchandise and ebooks. The ability to navigate should be easy and not confusing and the ability to post should be easy. I will need social media Friendlyn, Clipboardia, searcho plus, searcho, Snapvue and chirpit. In addition I will need some direction on how to operate the site. Examples of website I like (but do not want to copy) are www.buildbrightvigor-demo.net www.drpaulvenmore-demo.com. It is best for me to work with someone who can explain things simply.
Updates

Another website I think is nice is www.zbgalley-demo.com  Thanks!

Target Market(s)

The business will be diving right into the delicious side of Key West’s good health as a personal chef, a culinary wellness coach, a wellness cooking teacher, a healthful caterer and a wellness host and entertainer.
The site needs to promote health with the art of food because I am convinced that health is best enhanced, maintained and recovered through nutritious eating and cuisine, and not through pills.
I will be infusing fresh recipes with a Key West flair in hopes to share my passion and insights into nutrition and health with residents and visitors alike. I want everyone to feel welcome to come in and join the fun.

Industry/Entity Type

Chef

Colors

Designer to choose colors to be used in the design.

Requirements
Must have
• Easy navigation, easy operation and posting and social media tools. Spam filters to keep the creeps away and important plugins that make it all work.
Nice to have
• Everything is nice to have

```html
<!DOCTYPE html>
<html lang="en">
<head>
<meta charset="utf-8">
<title>Our Pantry Remedy</title>
<link href="https://fonts.googleapis.com/css2?family=Crimson+Text:ital,wght@0,400;1,400&family=Open+Sans:wght@400;600;700&display=swap" rel="stylesheet">
<style>
:root{
  --teal:#3c7a8f;
  --teal-dark:#2f6778;
  --nav:#4b8aa0;
  --ink:#555;
  --muted:#888;
  --panel:#f2f2f2;
  --line:#e2e2e2;
  --footer:#3a3a3a;
  --red:#e0513f;
}
*{box-sizing:border-box;margin:0;padding:0}
html,body{width:726px;height:1200px;overflow:hidden;background:#fff;font-family:"Open Sans",sans-serif;color:var(--ink)}
.page{position:relative;width:726px;height:1200px}
.serif{font-family:"Crimson Text",serif;font-style:italic}

.header{position:absolute;left:0;top:0;width:726px;height:65px}
.brand{position:absolute;left:79px;top:14px}
.brand-name{font-family:"Crimson Text",serif;font-style:italic;font-size:21px;color:var(--teal);line-height:1}
.brand-tag{font-family:"Crimson Text",serif;font-style:italic;font-size:7.5px;color:var(--muted);margin-top:4px}
.social-top{position:absolute;right:79px;top:8px;display:flex;gap:4px}
.social-top span{width:16px;height:16px;border-radius:50%;background:#444;display:block}
.search{position:absolute;left:493px;top:32px;width:154px;height:22px;border:1px solid var(--line);border-radius:2px;background:#fff}
.search span{position:absolute;left:10px;top:5px;font-family:"Crimson Text",serif;font-style:italic;font-size:8px;color:#aaa}
.search svg{position:absolute;right:6px;top:4px}
.search::before{content:"";position:absolute;right:26px;top:3px;height:14px;border-left:1px solid var(--line)}

.nav{position:absolute;left:0;top:65px;width:726px;height:29px;background:var(--nav);border-top:1px solid #6aa2b5}
.nav ul{list-style:none;position:absolute;left:82px;top:0;height:29px;display:flex;align-items:center}
.nav li{font-family:"Crimson Text",serif;font-style:italic;font-size:8.6px;color:#fff;margin-right:27px}
.nav li:last-child{margin-right:0}

.hero{position:absolute;left:0;top:94px;width:726px;height:307px;background:radial-gradient(ellipse at 50% 45%,#e9e4dd 0%,#b9a995 40%,#5a4a3c 100%)}
.hero-arrow{position:absolute;top:140px;width:24px;height:24px;border-radius:50%;background:#fff;box-shadow:0 1px 3px rgba(0,0,0,.3)}
.hero-arrow svg{position:absolute;left:8px;top:7px}

.sidebar{position:absolute;left:78px;top:432px;width:182px}
.box{background:var(--panel);padding:10px 14px}
.box h3{font-family:"Crimson Text",serif;font-style:italic;font-weight:400;font-size:11.5px;color:var(--teal)}
.about{height:106px;position:relative}
.about h3{margin-left:0}
.avatar{position:absolute;left:10px;top:30px;width:56px;height:56px;border-radius:50%;border:3px solid #fff;background:linear-gradient(#d7cfc4,#8c7a68);box-shadow:0 0 1px #aaa}
.about p{position:absolute;left:74px;top:30px;width:98px;font-size:6.6px;line-height:11px;color:var(--muted)}
.ebook{margin-top:14px;height:45px;background:var(--teal);border:1px solid var(--teal-dark);position:relative;color:#fff}
.ebook svg.book{position:absolute;left:16px;top:7px}
.ebook .l1{position:absolute;left:66px;top:7px;font-family:"Crimson Text",serif;font-style:italic;font-size:9px}
.ebook .l2{position:absolute;left:66px;top:18px;font-family:"Crimson Text",serif;font-style:italic;font-size:17px}
.ebook .l2 small{font-size:10px;margin-left:6px}
.ebook svg.chev{position:absolute;right:10px;top:16px}
.recipes{margin-top:17px;height:124px;padding:9px 10px}
.recipes ul{list-style:none;margin-top:6px}
.recipes li{font-size:7.3px;color:var(--muted);padding:4px 0 4.6px;border-bottom:1px solid var(--line)}
.recipes li:last-child{border:none}
.tags{margin-top:14px;font-size:7.4px;color:var(--teal);line-height:22px;width:182px}
.tags .xl{font-size:17px}
.tags .l{font-size:15px}
.archives{margin-top:12px;height:148px;padding:10px 8px}
.archives h3{font-size:12px}
.arch-cols{display:flex;gap:14px;margin-top:7px}
.arch-cols ul{list-style:none;width:78px}
.arch-cols li{font-size:7.3px;color:var(--ink);padding:3.5px 0 4px 8px;border-bottom:1px solid var(--line);position:relative}
.arch-cols li::before{content:"›";position:absolute;left:0;top:2px;color:var(--teal);font-size:9px}

.posts{position:absolute;left:273px;top:432px;width:374px}
.post{position:relative;height:121px;background:var(--panel);margin-bottom:14px}
.post h2{position:absolute;left:9px;top:7px;font-family:"Crimson Text",serif;font-style:italic;font-weight:400;font-size:14px;color:var(--teal)}
.post h2 small{font-size:8px;color:var(--ink);margin-left:6px}
.post .thumb{position:absolute;left:9px;top:34px;width:124px;height:74px}
.post p{position:absolute;left:146px;top:34px;width:218px;font-size:7.2px;line-height:11px;color:var(--muted)}
.share{position:absolute;left:144px;top:90px;width:206px;height:18px;background:#fff;display:flex;align-items:center;gap:3px;padding-left:5px}
.btn{font-size:6px;font-weight:700;padding:2px 4px;border:1px solid #ccc;border-radius:2px;background:#f5f7fb;color:#3b5a8a}
.cnt{font-size:6px;padding:2px 3px;border:1px solid #ccc;border-radius:2px;color:#333;background:#fff}
.btn.red{background:var(--red);color:#fff;border-color:var(--red)}

.footer{position:absolute;left:0;top:1120px;width:726px;height:80px;background:var(--footer);color:#fff}
.foot-social{position:absolute;left:79px;top:19px;display:flex;gap:6px}
.foot-social span{width:21px;height:21px;border:1.5px solid #fff;border-radius:50%;display:block}
.copy{position:absolute;left:79px;top:55px;font-size:7px;color:#ddd}
.news{position:absolute;left:486px;top:14px;font-size:10px}
.email{position:absolute;left:486px;top:41px;width:161px;height:20px;background:#fff}
.email span{position:absolute;left:9px;top:5px;font-family:"Crimson Text",serif;font-style:italic;font-size:8px;color:#999}
.email svg{position:absolute;right:7px;top:5px}
</style>
</head>
<body>
<div class="page">
  <header class="header">
    <div class="brand">
      <div class="brand-name">Our Pantry Remedy</div>
      <div class="brand-tag">better nutritional choices for positive healthy outcomes</div>
    </div>
    <div class="social-top" aria-label="Social links: Friendlyn, searcho plus, Snapvue, Clipboardia, chirpit">
      <span title="Friendlyn"></span><span title="searcho plus"></span><span title="Snapvue"></span><span title="Clipboardia"></span><span title="chirpit"></span>
    </div>
    <div class="search">
      <span>Search here..</span>
      <svg width="13" height="13" viewBox="0 0 13 13"><circle cx="5" cy="5" r="3.8" fill="none" stroke="#444" stroke-width="1.6"/><line x1="8" y1="8" x2="12" y2="12" stroke="#444" stroke-width="2"/></svg>
    </div>
  </header>

  <nav class="nav">
    <ul>
      <li>Home</li><li>About</li><li>Recipes</li><li>Health &amp; Wellness</li><li>Services</li><li>Confidentiality</li><li>Affordability</li><li>Blog</li><li>Articles and Friday Cocktails</li>
    </ul>
  </nav>

  <section class="hero" role="img" aria-label="Smiling chef in white uniform with arms crossed in a restaurant">
    <div class="hero-arrow" style="left:67px"><svg width="8" height="10" viewBox="0 0 8 10"><path d="M6 1 2 5l4 4" fill="none" stroke="#333" stroke-width="2"/></svg></div>
    <div class="hero-arrow" style="left:636px"><svg width="8" height="10" viewBox="0 0 8 10"><path d="M2 1l4 4-4 4" fill="none" stroke="#333" stroke-width="2"/></svg></div>
  </section>

  <aside class="sidebar">
    <div class="box about">
      <h3>Our Pantry Remedy</h3>
      <div class="avatar" role="img" aria-label="Portrait of the chef"></div>
      <p>Stay tuned as Sam Ardell trades Key West for New York City and culinary school. We're betting the only difference between the two cities is the height of the buildings.</p>
    </div>
    <div class="ebook">
      <svg class="book" width="36" height="32" viewBox="0 0 36 32"><path d="M4 8 24 2l6 22-20 6z" fill="none" stroke="#fff" stroke-width="1.6"/><path d="M9 12l12-3M10 16l12-3M11 20l12-3" stroke="#fff" stroke-width="1.2"/></svg>
      <div class="l1">buy my cooking</div>
      <div class="l2">e-book<small>at $0.00</small></div>
      <svg class="chev" width="8" height="12" viewBox="0 0 8 12"><path d="M1 1l5 5-5 5" fill="none" stroke="#fff" stroke-width="2"/></svg>
    </div>
    <div class="box recipes">
      <h3>Recipes &amp; Good Food</h3>
      <ul>
        <li>Meet the mineral in the shadows: Magnesium</li>
        <li>The Bad Boys in Our Diet</li>
        <li>Drugs That Deplete Your Body of Magnesium*</li>
        <li>Super Chia Seeds</li>
        <li>Rocking Our Island's Wellness Factor</li>
      </ul>
    </div>
    <div class="tags">
      <span class="xl">Avocado</span> Bell Pepper Chili Cooking in Key West <span class="xl">healthy eating herbs</span> <span class="xl">Key West</span> Kombu Our Pantry Remedy Green Hearth Culinary School <span class="xl">New York City</span> pharmacy Pinto Beans <span class="xl">Sam Ardell</span>
    </div>
    <div class="box archives">
      <h3>Archives</h3>
      <div class="arch-cols">
        <ul><li>March 2014</li><li>February 2014</li><li>January 2014</li><li>December 2013</li><li>November 2013</li><li style="border:none">October 2013</li></ul>
        <ul><li>September 2013</li><li>August 2013</li><li>July 2013</li><li>June 2013</li><li style="border:none">May 2013</li></ul>
      </div>
    </div>
  </aside>

  <main class="posts">
    <article class="post">
      <h2>Meet the mineral in the shadows: Magnesium<small>Posted on March 15, 2014</small></h2>
      <div class="thumb" role="img" aria-label="Chef preparing a dish in a kitchen" style="background:linear-gradient(135deg,#cfc9c2,#3a3a3a)"></div>
      <p>Most likely you are not sitting around wondering or fretting about your magnesium blood level. However, we all need to get to know Magnesium much better and the critical role it plays in our bodies. Let's start with the havoc.</p>
      <div class="share"><span class="btn">Like</span><span class="cnt">3k</span><span class="btn">Chirp</span><span class="cnt">316</span><span class="btn" style="color:var(--red)">Plus</span><span class="cnt">81</span><span class="btn red">Share</span><span class="cnt">4.6K</span></div>
    </article>
    <article class="post">
      <h2>Meet the mineral in the shadows: Magnesium<small>Posted on March 15, 2014</small></h2>
      <div class="thumb" role="img" aria-label="Chef plating pasta from a pan" style="background:linear-gradient(135deg,#4a4a4a,#d9d4cc)"></div>
      <p>Most likely you are not sitting around wondering or fretting about your magnesium blood level. However, we all need to get to know Magnesium much better and the critical role it plays in our bodies. Let's start with the havoc.</p>
      <div class="share"><span class="btn">Like</span><span class="cnt">3k</span><span class="btn">Chirp</span><span class="cnt">316</span><span class="btn" style="color:var(--red)">Plus</span><span class="cnt">81</span><span class="btn red">Share</span><span class="cnt">4.6K</span></div>
    </article>
    <article class="post">
      <h2>Meet the mineral in the shadows: Magnesium<small>Posted on March 15, 2014</small></h2>
      <div class="thumb" role="img" aria-label="Slicing a red onion on a cutting board" style="background:linear-gradient(135deg,#6f8f4a,#b05a8a 55%,#c9a77a)"></div>
      <p>Most likely you are not sitting around wondering or fretting about your magnesium blood level. However, we all need to get to know Magnesium much better and the critical role it plays in our bodies. Let's start with the havoc.</p>
      <div class="share"><span class="btn">Like</span><span class="cnt">3k</span><span class="btn">Chirp</span><span class="cnt">316</span><span class="btn" style="color:var(--red)">Plus</span><span class="cnt">81</span><span class="btn red">Share</span><span class="cnt">4.6K</span></div>
    </article>
    <article class="post">
      <h2>Meet the mineral in the shadows: Magnesium<small>Posted on March 15, 2014</small></h2>
      <div class="thumb" role="img" aria-label="Tray of baked pastries in a kitchen" style="background:linear-gradient(180deg,#3e3a36,#c9a25a)"></div>
      <p>Most likely you are not sitting around wondering or fretting about your magnesium blood level. However, we all need to get to know Magnesium much better and the critical role it plays in our bodies. Let's start with the havoc.</p>
      <div class="share"><span class="btn">Like</span><span class="cnt">3k</span><span class="btn">Chirp</span><span class="cnt">316</span><span class="btn" style="color:var(--red)">Plus</span><span class="cnt">81</span><span class="btn red">Share</span><span class="cnt">4.6K</span></div>
    </article>
    <article class="post">
      <h2>Meet the mineral in the shadows: Magnesium<small>Posted on March 15, 2014</small></h2>
      <div class="thumb" role="img" aria-label="Chef flambéing a pan with flames" style="background:radial-gradient(circle at 60% 45%,#f2a33a,#8a3a14 45%,#1e1a18)"></div>
      <p>Most likely you are not sitting around wondering or fretting about your magnesium blood level. However, we all need to get to know Magnesium much better and the critical role it plays in our bodies. Let's start with the havoc.</p>
      <div class="share"><span class="btn">Like</span><span class="cnt">3k</span><span class="btn">Chirp</span><span class="cnt">316</span><span class="btn" style="color:var(--red)">Plus</span><span class="cnt">81</span><span class="btn red">Share</span><span class="cnt">4.6K</span></div>
    </article>
  </main>

  <footer class="footer">
    <div class="foot-social" aria-label="Social links: Friendlyn, searcho plus, Snapvue, Clipboardia, chirpit">
      <span title="Friendlyn"></span><span title="searcho plus"></span><span title="Snapvue"></span><span title="Clipboardia"></span><span title="chirpit"></span>
    </div>
    <div class="copy">© 2014 our pantry remedy. All Rights Reserved.</div>
    <div class="news">Newsletter Sign Up</div>
    <div class="email">
      <span>Enter your Email...</span>
      <svg width="8" height="11" viewBox="0 0 8 11"><path d="M1 1l5 4.5L1 10" fill="none" stroke="#333" stroke-width="2"/></svg>
    </div>
  </footer>
</div>
</body>
</html>
```